Statement on the current financial and economic crisis, with a focus on Greece,

Anybody can become angry - that is easy, but to be angry with the right person and to the right degree and at the right time and for the right purpose, and in the right way - that is not within everybody's power and is not easy.
(Kelphinor ) greek philosopher

i want to do a poster with this words from Kelphinor greek philosopher and to show this statement for the greek people... its about for my project that i am doing.

Target Market(s)

my audience will be greek people but not only, from 18-80 years old for that reason i want my statement to be in english.

Industry/Entity Type

Financial

Requirements
Must have
• Anybody can become angry - that is easy, but to be angry with the right person and to the right degree and at the right time and for the right purpose, and in the right way - that is not within everybody's power and is not easy.
i want to show in my poster this statement from:
Kelphinor greek philosopher (384 – 322 BC)

```html
<!DOCTYPE html>
<html lang="en">
<head>
<meta charset="utf-8">
<title>Anybody Can Become Angry — Kelphinor</title>
<link rel="stylesheet" href="https://fonts.googleapis.com/css2?family=Jost:wght@800;900&display=swap">
<style>
  :root {
    --poster-red: #bd0b27;
    --ink: #121212;
    --paper: #ffffff;
  }
  * { margin: 0; padding: 0; box-sizing: border-box; }
  html, body {
    width: 900px;
    height: 1200px;
    overflow: hidden;
    background: var(--poster-red);
  }
  .poster {
    position: relative;
    width: 900px;
    height: 1200px;
    background: var(--poster-red);
    overflow: hidden;
  }
  .profile {
    position: absolute;
    top: 0;
    height: 1200px;
  }
  .profile--left {
    left: 0;
    width: 230px;
    background: linear-gradient(90deg, var(--paper) 0%, rgba(255,255,255,0.85) 45%, var(--poster-red) 100%);
  }
  .profile--right {
    right: 0;
    width: 250px;
    background: linear-gradient(270deg, var(--paper) 0%, rgba(255,255,255,0.85) 40%, var(--poster-red) 100%);
  }
  .quote {
    position: absolute;
    inset: 0;
    width: 900px;
    height: 1200px;
  }
  .quote text {
    font-family: "Jost", "Futura", sans-serif;
    fill: var(--ink);
    font-weight: 900;
    text-anchor: middle;
  }
  .quote .caps { font-weight: 800; }
  .quote .attribution { font-weight: 800; }
</style>
</head>
<body>
  <main class="poster">
    <div class="profile profile--left" role="img" aria-label="White silhouette of a face in profile, mouth open, shouting toward the right"></div>
    <div class="profile profile--right" role="img" aria-label="White silhouette of a face in profile, mouth open, shouting toward the left"></div>

    <svg class="quote" viewBox="0 0 900 1200" role="group" aria-label="Quotation by Kelphinor">
      <text class="caps" x="503" y="50"  font-size="52" textLength="290" lengthAdjust="spacingAndGlyphs">ANYBODY</text>
      <text class="caps" x="495" y="102" font-size="52" textLength="610" lengthAdjust="spacingAndGlyphs">CAN BECOME ANGRY</text>
      <text class="caps" x="505" y="152" font-size="52" textLength="444" lengthAdjust="spacingAndGlyphs">- THAT IS EASY,</text>
      <text x="505" y="211" font-size="62" textLength="116" lengthAdjust="spacingAndGlyphs">but</text>
      <text x="515" y="264" font-size="58" textLength="430" lengthAdjust="spacingAndGlyphs">to be angry</text>
      <text x="505" y="311" font-size="40" textLength="360" lengthAdjust="spacingAndGlyphs">with the right</text>
      <text x="497" y="372" font-size="92" textLength="315" lengthAdjust="spacingAndGlyphs">person</text>
      <text x="472" y="434" font-size="50" textLength="319" lengthAdjust="spacingAndGlyphs">and to the</text>
      <text x="452" y="518" font-size="98" textLength="245" lengthAdjust="spacingAndGlyphs">right</text>
      <text x="441" y="588" font-size="86" textLength="342" lengthAdjust="spacingAndGlyphs">degree</text>
      <text x="426" y="657" font-size="50" textLength="342" lengthAdjust="spacingAndGlyphs">and at the</text>
      <text x="419" y="728" font-size="92" textLength="472" lengthAdjust="spacingAndGlyphs">right time</text>
      <text x="351" y="789" font-size="44" textLength="432" lengthAdjust="spacingAndGlyphs">and for the right</text>
      <text x="486" y="858" font-size="104" textLength="447" lengthAdjust="spacingAndGlyphs">purpose,</text>
      <text x="319" y="914" font-size="44" textLength="265" lengthAdjust="spacingAndGlyphs">and in the</text>
      <text x="436" y="984" font-size="82" textLength="493" lengthAdjust="spacingAndGlyphs">right way</text>
      <text x="440" y="1052" font-size="44" textLength="474" lengthAdjust="spacingAndGlyphs">- that is not within</text>
      <text x="429" y="1095" font-size="42" textLength="478" lengthAdjust="spacingAndGlyphs">everybody's power</text>
      <text x="436" y="1142" font-size="44" textLength="392" lengthAdjust="spacingAndGlyphs">and is not easy</text>
      <text class="attribution" x="446" y="1189" font-size="26" textLength="492" lengthAdjust="spacingAndGlyphs">KELPHINOR (GREEK PHILOSOPHER)</text>
    </svg>
  </main>
</body>
</html>
```